Business Card Design Project

I own a dental practice and would like to use a logo that was recently designed to make business cards.
I am looking for a clean card with the following information on the card.

Halvorsen Dental Center (Using the logo)
Martin L. Halvorsen, D.D.S.
7234 Pinewick Ave. Suite B
Colorado Springs, CO 80547
(719) 482-6130
halvorsendentalcenter@mailbox-example.net
www.halvorsendentalcenter.example

Also a list of items on the back:
Services include

Family Dentistry
Cosmetic
Whitening
Tooth Colored Fillings
Crowns/Bridges
Implants/Tooth Replacement
Dentures
Root Canals
Updates

Just an FYI, I added an email address and website address.

I also added my Pic.  Please give designs with and without the pic

Thanks

Target Market(s)

20-70 U.S. Female that handles the household budget.

Industry/Entity Type

Dental

Requirements
Must have
• The logo is key. The color scheme of the logo is also key. The back of the business card should have the list of Dental Services offered at the practice. The front should be clean and professional looking. No cartoons. I will also include a picture of myself. I think that the final card may or may not include this picture, so the card designs should come with and without the picture. USE THE BLUE LOGO ONLY!!!
Should not have
• NO teeth should be on the card.

```html
<!DOCTYPE html>
<html lang="en">
<head>
<meta charset="utf-8">
<title>Halvorsen Dental Center – Business Card</title>
<link href="https://fonts.googleapis.com/css2?family=Arimo:wght@400&display=swap" rel="stylesheet">
<style>
  :root {
    --card-blue: #1f5878;
    --card-blue-soft: #2a6584;
    --ink-light: #c6d5de;
    --mark-tint: #9fb8c7;
    --photo-top: #3a7290;
    --photo-bottom: #2b6382;
    --gap-white: #ffffff;
  }
  * { margin: 0; padding: 0; box-sizing: border-box; }
  html, body {
    width: 933px;
    height: 1200px;
    overflow: hidden;
    background: var(--gap-white);
    font-family: "Arimo", Arial, sans-serif;
  }
  .sheet { position: relative; width: 933px; height: 1200px; }

  .card {
    position: absolute;
    left: 0;
    width: 933px;
    background: var(--card-blue);
    color: var(--ink-light);
  }
  .card--front { top: 0; height: 539px; }
  .card--back { top: 658px; height: 542px; overflow: hidden; }

  .contact {
    position: absolute;
    right: 46px;
    top: 40px;
    text-align: right;
    font-style: normal;
    font-size: 37px;
    line-height: 48.5px;
    white-space: nowrap;
  }
  .contact__web {
    font-size: 28px;
    line-height: 40px;
  }
  .contact__web:first-of-type { margin-top: 4px; }

  .brand {
    position: absolute;
    left: 34px;
    top: 372px;
    display: flex;
    align-items: center;
    gap: 22px;
  }
  .brand__dot {
    width: 80px;
    height: 80px;
    border-radius: 50%;
    background: var(--mark-tint);
    flex: none;
  }
  .brand__name {
    font-size: 46px;
    line-height: 52px;
    color: var(--mark-tint);
    white-space: nowrap;
  }

  .portrait {
    position: absolute;
    right: 46px;
    top: 360px;
    width: 120px;
    height: 148px;
    border-radius: 6px;
    background: linear-gradient(180deg, var(--photo-top), var(--photo-bottom));
  }

  .back-motif {
    position: absolute;
    left: 0;
    top: 0;
    width: 460px;
    height: 542px;
    background: radial-gradient(ellipse at 30% 40%, var(--card-blue-soft) 0%, var(--card-blue) 70%);
  }

  .services {
    position: absolute;
    right: 58px;
    top: 58px;
    list-style: none;
    text-align: right;
    font-size: 37.5px;
    line-height: 55.5px;
    white-space: nowrap;
  }
</style>
</head>
<body>
<div class="sheet">
  <section class="card card--front">
    <address class="contact">
      <div>Martin L. Halvorsen, D.D.S.</div>
      <div>7234 Pinewick Ave. Suite B</div>
      <div>Colorado Springs, CO 80547</div>
      <div>(719) 482-6130</div>
      <div class="contact__web">halvorsendentalcenter@mailbox-example.net</div>
      <div class="contact__web">www.halvorsendentalcenter.example</div>
    </address>
    <div class="brand">
      <span class="brand__dot"></span>
      <div class="brand__name">Halvorsen<br>Dental Center</div>
    </div>
    <div class="portrait" role="img" aria-label="Portrait photo of Dr. Martin L. Halvorsen"></div>
  </section>

  <section class="card card--back">
    <div class="back-motif" role="img" aria-label="Soft decorative background motif"></div>
    <ul class="services">
      <li>Family Dentistry</li>
      <li>Cosmetic</li>
      <li>Whitening</li>
      <li>Implants/Tooth Replacement</li>
      <li>Crowns/Bridges</li>
      <li>Tooth Colored Fillings</li>
      <li>Dentures</li>
      <li>Root Canals</li>
    </ul>
  </section>
</div>
</body>
</html>
```